Law Firm Website (Designed in Wix)

A website designed using my Wix account.
A website for a generalist law firm based in Melbourne, Australia.
The areas of practice include:
Criminal Law
Family Law
Civil Litigation
Wills & Probate
PELIX Claims
The colour theme will be green, black and white.
Website will require the following elements:
1. Chat box
2. General Description of the practice
3. Practice Areas (for selection)
4. Calendar bookings for Microsoft Outlook
5. Email enquiries
6. Telephone enquiries
7. Business location map
8. Videos
9. Photos

The following website can be used as inspiration, however I am looking for a copy and paste version of this site:
brunhollowadvocates.com

Target Market(s)

People requiring a Lawyer for Criminal, Family, Wills and Probabte, Conveyancing and Civil Litigstion Matters

Industry/Entity Type

Legal Sector

Coding

Coded - Design and coding required

Number of Pages Required

5+ page

Font styles to use
Other font styles liked:
• Based on business card

Requirements
Must have
• Colours and theme based on business card

```html
<!DOCTYPE html>
<html lang="en">
<head>
<meta charset="utf-8">
<title>Brunhollow Advocates</title>
<link href="https://fonts.googleapis.com/css2?family=Montserrat:wght@500;600;700&family=Roboto:wght@400;500;700&display=swap" rel="stylesheet">
<style>
:root{
  --green:#0b7d2b;
  --green-dark:#06641f;
  --black:#000;
  --ink:#1c1c1c;
  --muted:#6b6b6b;
  --light:#f2f2f2;
  --white:#fff;
  --navy:#1d2636;
  --footer:#1a1d22;
  --blue:#1a73e8;
  --blue-soft:#e8f0fe;
  --map-light:#ececec;
  --map-dark:#d4d4d4;
}
*{box-sizing:border-box;margin:0;padding:0}
html,body{width:1200px;height:4655px;overflow:hidden}
body{position:relative;background:var(--white);font-family:'Roboto',sans-serif;color:var(--ink)}
.abs{position:absolute}
.btn{display:inline-flex;align-items:center;gap:6px;background:var(--green);color:var(--white);font-family:'Roboto',sans-serif;font-weight:700;font-size:13px;text-transform:uppercase;border-radius:10px;padding:0 26px;height:46px;letter-spacing:.2px;white-space:nowrap}
.btn .dot{width:11px;height:11px;border-radius:50%;background:var(--white);display:inline-block;position:relative}
.btn .dot::after{content:"";position:absolute;left:4px;top:3px;border-left:4px solid var(--green);border-top:2.5px solid transparent;border-bottom:2.5px solid transparent}

/* header */
.site-header{left:0;top:0;width:1200px;height:105px;background:var(--green)}
.brand{left:118px;top:40px;color:var(--white);font-family:'Montserrat',sans-serif;font-weight:600;font-size:18px;letter-spacing:1px;text-align:center;line-height:1.2}
.brand small{display:block;font-size:11px;letter-spacing:4px}
.main-nav{left:468px;top:46px;display:flex;gap:30px;color:var(--white);font-size:13px;font-weight:700}
.main-nav .active{border-bottom:2px solid var(--white);padding-bottom:3px}
.search-btn{left:1032px;top:24px;width:58px;height:58px;background:var(--white);border-radius:10px;display:flex;align-items:center;justify-content:center}

/* hero */
.hero{left:0;top:105px;width:1200px;height:643px;background:linear-gradient(135deg,#5d6b5a 0%,#8a8e8c 35%,#6e7276 65%,#4a4f55 100%)}
.hero-title{left:0;top:425px;width:1200px;text-align:center;color:var(--white);font-family:'Montserrat',sans-serif;font-weight:700;font-size:50px}
.hero-btn{left:528px;top:514px}
.arrow-circle{width:44px;height:44px;border-radius:50%;background:rgba(255,255,255,.55);display:flex;align-items:center;justify-content:center}
.video-frame{left:213px;top:596px;width:774px;height:404px;background:var(--white);padding:10px 13px 4px}
.video-still{width:100%;height:100%;background:linear-gradient(160deg,#5a3a24 0%,#3a2618 45%,#1e2e26 100%);position:relative}
.play{position:absolute;width:66px;height:66px;border-radius:50%;background:var(--white);display:flex;align-items:center;justify-content:center}
.play::after{content:"";border-left:16px solid #111;border-top:10px solid transparent;border-bottom:10px solid transparent;margin-left:5px}

/* about */
.section-title{width:1200px;left:0;text-align:center;font-family:'Montserrat',sans-serif;font-weight:700;font-size:36px;color:var(--ink)}
.about-copy{left:170px;top:1084px;width:860px;text-align:center;font-size:13.5px;line-height:26px;color:var(--muted)}
.about-btn{left:520px;top:1182px}

/* testimonials */
.review{width:230px;height:242px;top:1314px;border:1px solid #ddd;padding:18px 18px}
.stars{display:flex;gap:2px;margin-bottom:16px}
.stars span{width:19px;height:19px;background:var(--green);display:flex;align-items:center;justify-content:center}
.review h3{font-size:16px;font-weight:500;line-height:26px;margin-bottom:8px}
.review p{font-size:12.5px;line-height:21px;color:var(--muted)}
.review .by{margin-top:10px;font-size:12.5px;color:var(--muted)}
.review .by b{color:var(--ink);font-weight:500}

/* stats */
.stats{left:0;top:1626px;width:1200px;height:280px;background:linear-gradient(180deg,#2c3648 0%,var(--navy) 50%,#161c28 100%)}
.stat{top:78px;width:300px;text-align:center;color:var(--white)}
.stat .pre{font-size:16px;letter-spacing:.5px}
.stat .num{font-weight:700;font-size:30px;margin:10px 0 12px}
.stat .post{font-size:16px;line-height:26px}

/* practice */
.practice{left:0;top:1906px;width:1200px;height:998px;background:var(--light)}
.area{width:312px;height:352px;background:var(--white);border-radius:14px;text-align:center;padding-top:28px}
.area svg{display:block;margin:0 auto}
.area h3{font-size:20px;font-weight:500;margin:20px 0 14px}
.area p{font-size:12.5px;line-height:26px;color:var(--muted);padding:0 22px}
.area .btn{margin-top:24px}

/* first steps */
.steps-title{left:0;top:2992px;width:1200px;text-align:center;font-family:'Montserrat',sans-serif;font-weight:700;font-size:38px;line-height:60px}
.steps{left:0;top:3184px;width:1200px;height:437px;background:var(--black)}
.step{top:0;width:304px;text-align:center;color:var(--white)}
.step-num{position:absolute;left:112px;top:-40px;width:80px;height:80px;border-radius:50%;background:var(--green);color:var(--white);font-family:'Montserrat',sans-serif;font-weight:700;font-size:36px;display:flex;align-items:center;justify-content:center}
.step h3{position:absolute;top:60px;width:100%;font-family:'Montserrat',sans-serif;font-weight:700;font-size:17px;white-space:nowrap}
.step .still{position:absolute;top:101px;width:304px;height:163px}
.step p{position:absolute;top:286px;width:100%;padding:0 14px;font-size:13.5px;line-height:22px}

/* contact */
.booking{left:112px;top:3782px;width:454px;height:488px;background:var(--white);box-shadow:0 2px 10px rgba(0,0,0,.12)}
.booking h3{text-align:center;font-size:21px;font-weight:400;margin-top:32px}
.month{position:absolute;left:54px;top:98px;color:#b06000;font-size:16px}
.cal-nav{position:absolute;right:60px;top:96px;display:flex;gap:24px;font-size:18px;color:#444}
.cal{position:absolute;left:52px;top:146px;width:352px;border-collapse:collapse}
.cal th{font-size:10px;font-weight:500;height:30px;color:#333}
.cal td{height:46px;text-align:center;font-size:11px;color:#555}
.cal td span{display:inline-flex;width:34px;height:34px;border-radius:50%;align-items:center;justify-content:center}
.cal td .open{background:var(--blue-soft);color:var(--blue);font-weight:700}
.cal td .pick{background:var(--blue);color:var(--white)}
.tz{position:absolute;left:64px;top:445px;font-size:9px;color:#333}
.office-map{left:629px;top:3822px;width:401px;height:388px;background:linear-gradient(180deg,var(--map-light),var(--map-dark))}
.chat{left:1055px;top:4321px;width:72px;height:72px;border-radius:50%;background:var(--white);box-shadow:0 2px 10px rgba(0,0,0,.2);display:flex;align-items:center;justify-content:center;z-index:2}

/* footer */
.site-footer{left:0;top:4355px;width:1200px;height:300px;background:linear-gradient(180deg,#2a2e35 0%,var(--footer) 100%);color:var(--white)}
.news-title{top:72px;width:1200px;text-align:center;font-family:'Montserrat',sans-serif;font-weight:700;font-size:21px}
.news-form{left:322px;top:119px;width:554px;height:42px;display:flex;border:3px solid var(--green);background:var(--white)}
.news-form span{flex:1;padding-left:20px;line-height:36px;font-size:13px;color:#666}
.news-form b{width:140px;background:var(--green);font-size:13px;text-align:center;line-height:36px}
.foot-nav{top:188px;width:1200px;text-align:center;font-size:13px;font-weight:700;word-spacing:4px}
.foot-nav i{font-style:normal;margin:0 14px;font-weight:400}
.copy{top:246px;width:1200px;text-align:center;font-size:12.5px}
</style>
</head>
<body>

<header class="abs site-header">
  <div class="abs brand">BRUNHOLLOW<small>ADVOCATES</small></div>
  <nav class="abs main-nav">
    <span class="active">HOME</span><span>ABOUT US</span><span>WHAT WE OFFER</span><span>TESTIMONIALS</span><span>CONTACT US</span>
  </nav>
  <div class="abs search-btn"><svg width="14" height="14" viewBox="0 0 14 14"><circle cx="6" cy="6" r="4.5" fill="none" stroke="#111" stroke-width="2"/><path d="M9.5 9.5 13 13" stroke="#111" stroke-width="2"/></svg></div>
</header>

<section class="abs hero" role="img" aria-label="Photo of three smiling lawyers in suits beside a green plant"></section>
<div class="abs arrow-circle" style="left:69px;top:402px"><svg width="10" height="10"><path d="M7 1 3 5l4 4" fill="none" stroke="#fff" stroke-width="1.6"/></svg></div>
<div class="abs arrow-circle" style="left:1085px;top:402px"><svg width="10" height="10"><path d="M3 1l4 4-4 4" fill="none" stroke="#fff" stroke-width="1.6"/></svg></div>
<h1 class="abs hero-title">BRUNHOLLOW ADVOCATES</h1>
<span class="abs btn hero-btn">Get Started</span>

<div class="abs video-frame">
  <div class="video-still" role="img" aria-label="Video still of a courtroom with a lawyer addressing the bench">
    <span class="play" style="left:341px;top:160px"></span>
  </div>
</div>

<h2 class="abs section-title" style="top:1026px">ABOUT US</h2>
<p class="abs about-copy">Lorem ipsum dolor sit amet, consectetur adipiscing elit, sed do eiusmod tempor incididunt ut labore et dolore magna aliqua. Ut enim ad minim veniam, quis nostrud exercitation ullamco laboris nisi ut aliquip ex ea comm odo consequat. Duis aute irure dolor in reprehenderit in voluptate velit esse cillum dolore eu fugiat nulla pariatur.</p>
<span class="abs btn about-btn">Laern More <i class="dot"></i></span>

<article class="abs review" style="left:110px">
  <div class="stars"><span><svg width="11" height="11" viewBox="0 0 10 10"><path d="M5 .5l1.3 3H9.5L7 5.5l1 3.3L5 7 2 8.8l1-3.3L.5 3.5h3.2z" fill="#fff"/></svg></span><span><svg width="11" height="11" viewBox="0 0 10 10"><path d="M5 .5l1.3 3H9.5L7 5.5l1 3.3L5 7 2 8.8l1-3.3L.5 3.5h3.2z" fill="#fff"/></svg></span><span><svg width="11" height="11" viewBox="0 0 10 10"><path d="M5 .5l1.3 3H9.5L7 5.5l1 3.3L5 7 2 8.8l1-3.3L.5 3.5h3.2z" fill="#fff"/></svg></span><span><svg width="11" height="11" viewBox="0 0 10 10"><path d="M5 .5l1.3 3H9.5L7 5.5l1 3.3L5 7 2 8.8l1-3.3L.5 3.5h3.2z" fill="#fff"/></svg></span><span><svg width="11" height="11" viewBox="0 0 10 10"><path d="M5 .5l1.3 3H9.5L7 5.5l1 3.3L5 7 2 8.8l1-3.3L.5 3.5h3.2z" fill="#fff"/></svg></span></div>
  <h3>Duis aute irure dolor reprehenderit</h3>
  <p>Lorem ipsum dolor sit amet, consectetur adipiscing elit, sed do eiusmod tempor incididunt ut labore et dolore aliqua.</p>
  <div class="by"><b>A.K.</b> Sep 11</div>
</article>
<article class="abs review" style="left:360px">
  <div class="stars"><span><svg width="11" height="11" viewBox="0 0 10 10"><path d="M5 .5l1.3 3H9.5L7 5.5l1 3.3L5 7 2 8.8l1-3.3L.5 3.5h3.2z" fill="#fff"/></svg></span><span><svg width="11" height="11" viewBox="0 0 10 10"><path d="M5 .5l1.3 3H9.5L7 5.5l1 3.3L5 7 2 8.8l1-3.3L.5 3.5h3.2z" fill="#fff"/></svg></span><span><svg width="11" height="11" viewBox="0 0 10 10"><path d="M5 .5l1.3 3H9.5L7 5.5l1 3.3L5 7 2 8.8l1-3.3L.5 3.5h3.2z" fill="#fff"/></svg></span><span><svg width="11" height="11" viewBox="0 0 10 10"><path d="M5 .5l1.3 3H9.5L7 5.5l1 3.3L5 7 2 8.8l1-3.3L.5 3.5h3.2z" fill="#fff"/></svg></span><span><svg width="11" height="11" viewBox="0 0 10 10"><path d="M5 .5l1.3 3H9.5L7 5.5l1 3.3L5 7 2 8.8l1-3.3L.5 3.5h3.2z" fill="#fff"/></svg></span></div>
  <h3>Duis aute irure dolor reprehenderit</h3>
  <p>Lorem ipsum dolor sit amet, consectetur adipiscing elit, sed do eiusmod tempor incididunt ut labore et dolore aliqua.</p>
  <div class="by"><b>S.K.</b> Sep 11</div>
</article>
<article class="abs review" style="left:609px">
  <div class="stars"><span><svg width="11" height="11" viewBox="0 0 10 10"><path d="M5 .5l1.3 3H9.5L7 5.5l1 3.3L5 7 2 8.8l1-3.3L.5 3.5h3.2z" fill="#fff"/></svg></span><span><svg width="11" height="11" viewBox="0 0 10 10"><path d="M5 .5l1.3 3H9.5L7 5.5l1 3.3L5 7 2 8.8l1-3.3L.5 3.5h3.2z" fill="#fff"/></svg></span><span><svg width="11" height="11" viewBox="0 0 10 10"><path d="M5 .5l1.3 3H9.5L7 5.5l1 3.3L5 7 2 8.8l1-3.3L.5 3.5h3.2z" fill="#fff"/></svg></span><span><svg width="11" height="11" viewBox="0 0 10 10"><path d="M5 .5l1.3 3H9.5L7 5.5l1 3.3L5 7 2 8.8l1-3.3L.5 3.5h3.2z" fill="#fff"/></svg></span><span><svg width="11" height="11" viewBox="0 0 10 10"><path d="M5 .5l1.3 3H9.5L7 5.5l1 3.3L5 7 2 8.8l1-3.3L.5 3.5h3.2z" fill="#fff"/></svg></span></div>
  <h3>Duis aute irure dolor reprehenderit</h3>
  <p>Lorem ipsum dolor sit amet, consectetur adipiscing elit, sed do eiusmod tempor incididunt ut labore et dolore aliqua.</p>
  <div class="by"><b>A.K.</b> Sep 11</div>
</article>
<article class="abs review" style="left:858px">
  <div class="stars"><span><svg width="11" height="11" viewBox="0 0 10 10"><path d="M5 .5l1.3 3H9.5L7 5.5l1 3.3L5 7 2 8.8l1-3.3L.5 3.5h3.2z" fill="#fff"/></svg></span><span><svg width="11" height="11" viewBox="0 0 10 10"><path d="M5 .5l1.3 3H9.5L7 5.5l1 3.3L5 7 2 8.8l1-3.3L.5 3.5h3.2z" fill="#fff"/></svg></span><span><svg width="11" height="11" viewBox="0 0 10 10"><path d="M5 .5l1.3 3H9.5L7 5.5l1 3.3L5 7 2 8.8l1-3.3L.5 3.5h3.2z" fill="#fff"/></svg></span><span><svg width="11" height="11" viewBox="0 0 10 10"><path d="M5 .5l1.3 3H9.5L7 5.5l1 3.3L5 7 2 8.8l1-3.3L.5 3.5h3.2z" fill="#fff"/></svg></span><span><svg width="11" height="11" viewBox="0 0 10 10"><path d="M5 .5l1.3 3H9.5L7 5.5l1 3.3L5 7 2 8.8l1-3.3L.5 3.5h3.2z" fill="#fff"/></svg></span></div>
  <h3>Duis aute irure dolor reprehenderit</h3>
  <p>Lorem ipsum dolor sit amet, consectetur adipiscing elit, sed do eiusmod tempor incididunt ut labore et dolore aliqua.</p>
  <div class="by"><b>S.K.</b> Sep 11</div>
</article>

<section class="abs stats" role="img" aria-label="Night view of tall city office towers, darkened">
  <div class="abs stat" style="left:94px"><div class="pre">OVER</div><div class="num">57,065</div><div class="post">COURTROOM<br>HOURS</div></div>
  <div class="abs stat" style="left:445px"><div class="pre">MORE THAN</div><div class="num">57,065</div><div class="post">CLIENTS HELPED</div></div>
  <div class="abs stat" style="left:797px"><div class="pre">WE HAVE</div><div class="num">42+</div><div class="post">YEARS OF CRIMINAL<br>DEFNCE EXPERIENCE</div></div>
</section>

<section class="abs practice">
  <h2 class="abs section-title" style="top:88px">PRACTICE AREAS</h2>

  <article class="abs area" style="left:110px;top:158px">
    <svg width="72" height="82" viewBox="0 0 72 82" fill="none" stroke="#0b7d2b" stroke-width="2.5"><rect x="4" y="4" width="64" height="74" rx="2"/><rect x="12" y="12" width="48" height="58"/><path d="M36 22v36M24 30h24M24 30l-6 14h12zM48 30l-6 14h12zM28 60h16"/></svg>
    <h3>Criminal Law</h3>
    <p>Lorem ipsum dolor sit amet, consect etur adipiscing elit, sed do eiusmod tempor incididunt ut labore et dolore</p>
    <span class="btn">Laern More <i class="dot"></i></span>
  </article>
  <article class="abs area" style="left:444px;top:158px">
    <svg width="66" height="82" viewBox="0 0 66 82" fill="none" stroke="#0b7d2b" stroke-width="2.5"><path d="M33 4v34M13 12h40M13 12l-8 16h16zM53 12l-8 16h16z"/><circle cx="21" cy="50" r="6"/><circle cx="45" cy="50" r="6"/><circle cx="33" cy="62" r="6"/><path d="M8 78c0-10 26-10 26 0M32 78c0-10 26-10 26 0"/></svg>
    <h3>Family Law</h3>
    <p>Lorem ipsum dolor sit amet, consect etur adipiscing elit, sed do eiusmod tempor incididunt ut labore et dolore</p>
    <span class="btn">Laern More <i class="dot"></i></span>
  </article>
  <article class="abs area" style="left:777px;top:158px">
    <svg width="80" height="82" viewBox="0 0 80 82" fill="none" stroke="#0b7d2b" stroke-width="2.5"><circle cx="40" cy="12" r="8"/><path d="M40 20v48M12 28h56M12 28l-9 18h18zM68 28l-9 18h18zM22 70h36v8H22z"/></svg>
    <h3>Civil Litigation</h3>
    <p>Lorem ipsum dolor sit amet, consect etur adipiscing elit, sed do eiusmod tempor incididunt ut labore et dolore</p>
    <span class="btn">Laern More <i class="dot"></i></span>
  </article>
  <article class="abs area" style="left:278px;top:535px">
    <svg width="72" height="82" viewBox="0 0 72 82" fill="none" stroke="#0b7d2b" stroke-width="2.5"><rect x="18" y="4" width="50" height="74" rx="2"/><path d="M28 18h30M28 28h30M28 38h30M28 48h20"/><path d="M4 30h16v26l-8 6-8-6z"/><path d="M8 44l3 3 6-7"/></svg>
    <h3>Wills &amp; Probate</h3>
    <p>Lorem ipsum dolor sit amet, consect etur adipiscing elit, sed do eiusmod tempor incididunt ut labore et dolore</p>
    <span class="btn">Laern More <i class="dot"></i></span>
  </article>
  <article class="abs area" style="left:611px;top:535px">
    <svg width="76" height="82" viewBox="0 0 76 82" fill="none" stroke="#0b7d2b" stroke-width="2.5"><rect x="28" y="10" width="44" height="62" rx="2"/><path d="M38 24h24M38 34h24M38 44h16"/><circle cx="20" cy="18" r="8"/><path d="M4 78V54c0-8 32-8 32 0v24z"/><path d="M14 64l4 4 8-8"/></svg>
    <h3>PELIX Claims</h3>
    <p>Lorem ipsum dolor sit amet, consect etur adipiscing elit, sed do eiusmod tempor incididunt ut labore et dolore</p>
    <span class="btn">Laern More <i class="dot"></i></span>
  </article>
</section>

<h2 class="abs steps-title">FIRST STEPS WHEN FACING A<br>CRIMINAL CHARGE</h2>
<section class="abs steps">
  <div class="abs step" style="left:110px">
    <span class="step-num">1</span>
    <h3>DUIS AUTE IRURE DOLOR</h3>
    <div class="still" role="img" aria-label="Video still of a lawyer signing papers at a desk" style="background:linear-gradient(135deg,#3a2a1c,#8b7354 55%,#e3dccf)"><span class="play" style="left:119px;top:48px"></span></div>
    <p>Lorem ipsum dolor sit amet, consectetur adipiscing elit, sed do eiusmod tempor incididunt</p>
  </div>
  <div class="abs step" style="left:448px">
    <span class="step-num">2</span>
    <h3>DUIS AUTE IRURE DOLOR</h3>
    <div class="still" role="img" aria-label="Video still of a man in a suit reviewing documents" style="background:linear-gradient(135deg,#d8d4cd,#6d6a66 55%,#f2f0ec)"><span class="play" style="left:119px;top:48px"></span></div>
    <p>Lorem ipsum dolor sit amet, consectetur adipiscing elit, sed do eiusmod tempor incididunt</p>
  </div>
  <div class="abs step" style="left:786px">
    <span class="step-num">3</span>
    <h3>DUIS AUTE IRURE DOLOR</h3>
    <div class="still" role="img" aria-label="Video still of a client meeting a lawyer in an office" style="background:linear-gradient(135deg,#e9eef3,#7c8c9c 50%,#2b3a52)"><span class="play" style="left:119px;top:48px"></span></div>
    <p>Lorem ipsum dolor sit amet, consectetur adipiscing elit, sed do eiusmod tempor incididunt</p>
  </div>
</section>

<h2 class="abs section-title" style="top:3704px">CONTACT US</h2>
<div class="abs booking">
  <h3>Select A Day</h3>
  <div class="month">September 2023</div>
  <div class="cal-nav"><span>‹</span><span style="color:#b06000">›</span></div>
  <table class="cal">
    <tr><th>SUN</th><th>MON</th><th>TUE</th><th>WED</th><th>THU</th><th>FRI</th><th>SAT</th></tr>
    <tr><td></td><td></td><td></td><td></td><td></td><td><span>1</span></td><td><span>2</span></td></tr>
    <tr><td><span>3</span></td><td><span>4</span></td><td><span>5</span></td><td><span>6</span></td><td><span class="pick">7</span></td><td><span class="open">8</span></td><td><span>9</span></td></tr>
    <tr><td><span>10</span></td><td><span class="open">11</span></td><td><span>12</span></td><td><span class="open">13</span></td><td><span class="open">14</span></td><td><span class="open">15</span></td><td><span>16</span></td></tr>
    <tr><td><span>17</span></td><td><span class="open">18</span></td><td><span>19</span></td><td><span class="open">20</span></td><td><span class="open">21</span></td><td><span class="open">22</span></td><td><span>23</span></td></tr>
    <tr><td><span>24</span></td><td><span class="open">25</span></td><td><span>26</span></td><td><span class="open">27</span></td><td><span class="open">28</span></td><td><span class="open">29</span></td><td><span>30</span></td></tr>
  </table>
  <div class="tz">◉ &nbsp;Eastern Time - US &amp; Canada (4:34pm) ▾</div>
</div>
<div class="abs office-map" role="img" aria-label="Map placeholder: dotted map of the country showing the office locations"></div>

<div class="abs chat"><svg width="26" height="24" viewBox="0 0 26 24"><path d="M13 2C6.4 2 1 6.2 1 11.5c0 3 1.7 5.6 4.4 7.3L4 23l5.2-2.6c1.2.3 2.5.5 3.8.5 6.6 0 12-4.2 12-9.4S19.6 2 13 2z" fill="#111"/></svg></div>

<footer class="abs site-footer" role="img" aria-label="Dimmed city skyline at dusk behind the newsletter signup">
  <h2 class="abs news-title">SUBSCRIBE TO OUR NEWSLETTER</h2>
  <div class="abs news-form"><span>Emai address</span><b>SUBSCRIBE</b></div>
  <nav class="abs foot-nav">HOME<i>/</i>ABOUT US<i>/</i>WHAT WE OFFER<i>/</i>TESTIMONIALS<i>/</i>CONTACT US</nav>
  <div class="abs copy">© COPYRIGHTS 2023 ALL RIGHTS RESERVED &nbsp;|&nbsp; TERMS &nbsp;|&nbsp; PRIVACY &nbsp;|&nbsp; DISCLAIMER</div>
</footer>

</body>
</html>
```